Peter + Rob's 30th Birthday FB event cover photo

We're after a Facebook even cover photo for our 30th B'day. We live in Sydney
Peter + Rob's 30th Birthday

Venue (these details can be used in the graphic):
Quiet Heron
the basement of
The Marlow Hotel
42 Brackley St Fernhill
2 August 8pm-3am

The Marlow logo: http://www.themarlowhotelqz.com
Quiet Heron logo: http://quietheronpurrqz.com.au
The horizontal FaceBook cover photo for events has specific dimensions
As ideas I kind of like the styling of the dj poster (file attached) as a rough guide but not essential (i.e. no need to stick to that format/colours/dark shades) and Also the poster Pixel Harbour's Bruno did for Lumen Run
Thanks!

```html
<!DOCTYPE html>
<html lang="en">
<head>
<meta charset="utf-8">
<title>Peter + Rob's 30th Birthday</title>
<link rel="stylesheet" href="https://fonts.googleapis.com/css2?family=Bebas+Neue&family=Oswald:wght@400;500&display=swap">
<style>
  :root {
    --night: #1c0f1a;
    --plum: #4a2447;
    --rose: #b04a86;
    --amber: #c96a2e;
    --teal: #2f6a78;
    --white: #ffffff;
    --ink: #3b2418;
    --ink-warm: #6b3a1d;
  }
  html, body {
    margin: 0;
    padding: 0;
    width: 1200px;
    height: 452px;
    overflow: hidden;
    background: var(--night);
  }
  .cover {
    position: relative;
    width: 1200px;
    height: 452px;
    overflow: hidden;
    font-family: "Bebas Neue", "Oswald", sans-serif;
    color: var(--white);
  }
  .cover__backdrop {
    position: absolute;
    inset: 0;
    background:
      radial-gradient(ellipse 260px 180px at 120px 340px, rgba(176, 74, 134, 0.75), transparent 70%),
      radial-gradient(ellipse 220px 160px at 360px 400px, rgba(201, 106, 46, 0.55), transparent 70%),
      radial-gradient(ellipse 200px 140px at 300px 120px, rgba(47, 106, 120, 0.55), transparent 70%),
      radial-gradient(ellipse 260px 200px at 900px 180px, rgba(201, 106, 46, 0.55), transparent 70%),
      radial-gradient(ellipse 300px 180px at 1050px 420px, rgba(176, 74, 134, 0.7), transparent 70%),
      radial-gradient(ellipse 200px 120px at 1150px 60px, rgba(74, 36, 71, 0.9), transparent 70%),
      linear-gradient(180deg, #2a1526 0%, var(--plum) 55%, #5a2a55 100%);
  }
  .cover__strings {
    position: absolute;
    inset: 0;
  }
  .cover__strings line {
    stroke: rgba(255, 255, 255, 0.8);
    stroke-width: 1.6;
    stroke-dasharray: 5 5;
  }
  .badge {
    position: absolute;
    left: 420px;
    top: 42px;
    width: 362px;
    height: 362px;
    border-radius: 50%;
    background: var(--white);
    display: flex;
    flex-direction: column;
    align-items: center;
    justify-content: center;
    color: var(--ink);
  }
  .badge__names {
    font-size: 60px;
    line-height: 1;
    letter-spacing: 0.5px;
    color: var(--ink-warm);
    margin-top: 6px;
  }
  .badge__age {
    font-size: 162px;
    line-height: 0.8;
    letter-spacing: 1px;
    margin-top: 6px;
  }
  .badge__word {
    font-size: 92px;
    line-height: 0.9;
    letter-spacing: 1px;
    margin-top: 4px;
  }
  .venue {
    position: absolute;
    left: 23px;
    top: 160px;
  }
  .venue__name {
    font-size: 68px;
    line-height: 1;
    font-style: italic;
    letter-spacing: 0.5px;
  }
  .venue__address {
    font-family: "Oswald", sans-serif;
    font-weight: 500;
    font-size: 27px;
    line-height: 1;
    margin-top: 12px;
    letter-spacing: 0.3px;
  }
  .when {
    position: absolute;
    right: 20px;
    top: 150px;
    text-align: right;
  }
  .when__date {
    font-size: 58px;
    line-height: 1;
    letter-spacing: 0.5px;
  }
  .when__time {
    font-size: 86px;
    line-height: 1;
    letter-spacing: 0.5px;
    margin-top: 2px;
  }
</style>
</head>
<body>
  <main class="cover">
    <div class="cover__backdrop" role="img" aria-label="Blurred night-time city lights in pink, amber and teal bokeh"></div>

    <svg class="cover__strings" width="1200" height="452" viewBox="0 0 1200 452" aria-hidden="true">
      <line x1="0" y1="26" x2="1200" y2="14"/>
      <line x1="0" y1="70" x2="1200" y2="92"/>
      <line x1="0" y1="94" x2="1200" y2="84"/>
      <line x1="0" y1="148" x2="1200" y2="140"/>
      <line x1="0" y1="318" x2="1200" y2="332"/>
      <line x1="0" y1="352" x2="1200" y2="344"/>
      <line x1="0" y1="398" x2="1200" y2="414"/>
      <line x1="0" y1="430" x2="1200" y2="422"/>
    </svg>

    <section class="venue">
      <div class="venue__name">QUIET HERON</div>
      <div class="venue__address">42 BRACKLEY ST. FERNHILL</div>
    </section>

    <section class="badge">
      <div class="badge__names">PETER+ROB'S</div>
      <div class="badge__age">30TH</div>
      <div class="badge__word">BIRTHDAY</div>
    </section>

    <section class="when">
      <div class="when__date">2ND AUGUST</div>
      <div class="when__time">8PM-3AM</div>
    </section>
  </main>
</body>
</html>
```